Harwick Assurance Partners Ltd needs a business card and logo

We need a logo for documents, invoices etc and a business card to match. We are a health auditing, training and consulting company based in NZ and working in both Australia and NZ. We ensure health organisations meet all their compliance requirements and develop expertise in the health auditing sector. The design should in some way reflect either symbols for quality management in the health sector.

Target Market(s)

Health providers and those wishing to increase their capability in meeting and understanding compliance requirements

Industry/Entity Type

Business

Contact Information for Business Card

Logo plus contact details

Logo Text

Health auditing, consultancy and training

Requirements
Must have
• Name and contact details director: Molly Strand, mstrand@hap-example.co.nz, PO Box 318, Warkworth, NZ, cell +6427391065

```html
<!DOCTYPE html>
<html lang="en">
<head>
<meta charset="utf-8">
<title>Harwick Assurance Partners Ltd – Business Card</title>
<link rel="stylesheet" href="https://fonts.googleapis.com/css2?family=Montserrat:wght@400;500&display=swap">
<style>
  :root {
    --stage: #2b2b2b;
    --card-white: #f7f7f5;
    --brand-blue: #2a8fd0;
    --deep-blue: #1f7cc4;
    --sky-blue: #35a9d8;
    --leaf-green: #52b84e;
    --text-white: #ffffff;
  }
  * { box-sizing: border-box; margin: 0; padding: 0; }
  html, body {
    width: 1200px; height: 900px; overflow: hidden;
    background: var(--stage);
    font-family: "Montserrat", sans-serif;
  }
  .stage {
    width: 1200px; height: 900px;
    display: flex; flex-direction: column;
    align-items: center; justify-content: center; gap: 60px;
  }
  .card {
    position: relative;
    width: 640px; height: 366px;
    overflow: hidden;
    box-shadow: 0 10px 30px rgba(0,0,0,0.45);
  }
  /* Back of card */
  .card--back {
    background: linear-gradient(135deg, var(--sky-blue) 0%, var(--deep-blue) 70%);
    display: flex; align-items: center; justify-content: center;
  }
  .brand {
    display: flex; align-items: center; gap: 14px;
    font-weight: 500; letter-spacing: 0.12em; text-transform: uppercase;
    line-height: 1.25;
  }
  .brand__dot {
    flex: none; border-radius: 50%;
  }
  .card--back .brand { color: var(--text-white); font-size: 24px; }
  .card--back .brand__dot { width: 62px; height: 62px; background: var(--text-white); }

  /* Front of card */
  .card--front { background: var(--card-white); }
  .card__waves { position: absolute; inset: 0; }
  .card--front .brand {
    position: absolute; top: 44px; right: 40px;
    color: var(--brand-blue); font-size: 17px;
  }
  .card--front .brand__dot { width: 44px; height: 44px; background: var(--brand-blue); }
  .contact {
    position: absolute; left: 58px; top: 262px;
    color: var(--text-white);
  }
  .contact__name {
    font-size: 17px; font-weight: 500; letter-spacing: 0.06em;
    text-transform: uppercase; margin-bottom: 12px;
  }
  .contact__line { font-size: 15px; font-weight: 400; line-height: 1.45; }
  .contact__label { display: inline-block; width: 26px; }
  .address {
    position: absolute; right: 38px; top: 236px;
    color: var(--text-white); font-size: 14px; font-weight: 400;
  }
</style>
</head>
<body>
<main class="stage">
  <section class="card card--back" aria-label="Card back">
    <div class="brand">
      <span class="brand__dot"></span>
      <span>Harwick Assurance<br>Partners Ltd</span>
    </div>
  </section>

  <section class="card card--front" aria-label="Card front">
    <svg class="card__waves" viewBox="0 0 640 366" width="640" height="366" aria-hidden="true">
      <defs>
        <linearGradient id="bandBlue" x1="0" y1="0" x2="1" y2="1">
          <stop offset="0" stop-color="#2a8fd0"/>
          <stop offset="0.5" stop-color="#35a9d8"/>
          <stop offset="1" stop-color="#1f7cc4"/>
        </linearGradient>
      </defs>
      <path d="M300,205 C460,198 565,150 640,62 L640,76 C565,160 460,205 300,205Z" fill="#2a8fd0"/>
      <path d="M0,220 C200,190 430,198 640,84 L640,96 C430,210 200,204 0,232Z" fill="#52b84e"/>
      <path d="M0,230 C200,202 430,208 640,94 L640,366 L0,366Z" fill="url(#bandBlue)"/>
    </svg>

    <div class="brand">
      <span class="brand__dot"></span>
      <span>Harwick Assurance<br>Partners Ltd</span>
    </div>

    <div class="contact">
      <p class="contact__name">Molly Strand</p>
      <p class="contact__line"><span class="contact__label">M:</span>+6427391065</p>
      <p class="contact__line"><span class="contact__label">E:</span>mstrand@hap-example.co.nz</p>
    </div>

    <p class="address">PO Box 318, Warkworth, NZ</p>
  </section>
</main>
</body>
</html>
```